Tidewell Vertical Estate Council revised design

We need a logo for our email and letterhead design. We are a non-profit home owners association looking to look a little more professional. Attached is our current "logo" but it doesn't work well with letters or email. We would like to stay with the same concept.

Target Market(s)

Home owners, attorney, bankers, legislators

Industry/Entity Type

Non Profit

Font styles to use
Sans Serif

Colors

Designer to choose colors to be used in the design.

Requirements
Must have
• Company name: Tidewell Vertical Estate Council
Nice to have
• This will always be on a while background (paper or email)

```html
<!DOCTYPE html>
<html lang="en">
<head>
<meta charset="utf-8">
<title>Tidewell Vertical Estate Council – Stationery</title>
<link rel="stylesheet" href="https://fonts.googleapis.com/css2?family=Open+Sans:wght@400;600;700&display=swap">
<style>
  :root {
    --stage: #636363;
    --paper: #ffffff;
    --taupe: #776858;
    --taupe-dark: #5e5246;
    --taupe-fold: #3d352d;
    --slate: #8a979b;
    --slate-light: #d3d6d5;
    --ink-grey: #8d9396;
    --window-line: #b9bcbd;
    --white: #ffffff;
  }
  * { box-sizing: border-box; margin: 0; padding: 0; }
  html, body { width: 1200px; height: 821px; overflow: hidden; background: var(--stage); }
  body { font-family: "Open Sans", Arial, sans-serif; position: relative; }

  .sheet { position: absolute; background: var(--paper); overflow: hidden; }
  .letterhead { left: 22px; top: 20px; width: 553px; height: 773px; }
  .card-front { left: 585px; top: 20px; width: 246px; height: 143px; }
  .card-back { left: 922px; top: 20px; width: 245px; height: 143px; }
  .envelope-front { left: 583px; top: 174px; width: 585px; height: 299px; }
  .envelope-back { left: 583px; top: 485px; width: 585px; height: 308px; }

  /* Wordmark */
  .wordmark {
    position: absolute; display: flex; align-items: center; gap: 6%;
    padding: 0 6%;
    color: var(--taupe); font-weight: 700; text-transform: uppercase;
    line-height: 1.1; letter-spacing: 0.02em;
  }
  .wordmark-square { flex: none; background: var(--taupe); }

  .letterhead .wordmark { left: 431px; top: 27px; width: 94px; height: 57px; font-size: 9px; }
  .letterhead .wordmark-square { width: 12px; height: 12px; }
  .card-front .wordmark { left: 86px; top: 39px; width: 75px; height: 46px; font-size: 7px; }
  .card-front .wordmark-square { width: 9px; height: 9px; }
  .card-back .wordmark { left: 167px; top: 18px; width: 56px; height: 33px; font-size: 5px; }
  .card-back .wordmark-square { width: 6px; height: 6px; }
  .envelope-front .wordmark { left: 42px; top: 32px; width: 101px; height: 61px; font-size: 9.5px; }
  .envelope-front .wordmark-square { width: 13px; height: 13px; }
  .envelope-back .wordmark { left: 243px; top: 159px; width: 101px; height: 62px; font-size: 9.5px; }
  .envelope-back .wordmark-square { width: 13px; height: 13px; }

  /* Contact band */
  .contact-band {
    position: absolute; left: 0; right: 0; bottom: 0;
    background: radial-gradient(ellipse 40% 140% at 52% 50%, var(--slate-light), var(--slate) 80%);
    color: var(--white); font-size: 8.8px;
  }
  .letterhead .contact-band { height: 46px; }
  .envelope-front .contact-band { height: 41px; }
  .contact-item {
    position: absolute; top: 50%; transform: translateY(-50%);
    display: flex; align-items: center; gap: 5px; white-space: nowrap;
  }
  .icon { width: 12px; height: 12px; flex: none; }
  .letterhead .contact-item.address { left: 25px; }
  .letterhead .contact-item.phone { left: 296px; }
  .letterhead .contact-item.email { left: 414px; }
  .envelope-front .contact-item.address { left: 27px; }
  .envelope-front .contact-item.phone { left: 325px; }
  .envelope-front .contact-item.email { left: 444px; }

  .web-tab {
    position: absolute; z-index: 2; left: 208px; top: 714px; width: 138px; height: 23px;
    background: var(--taupe); color: var(--white); font-size: 9px;
    display: flex; align-items: center; justify-content: center;
    border-radius: 0 0 6px 6px;
  }
  .web-tab-fold { position: absolute; z-index: 2; top: 714px; width: 10px; height: 13px; }
  .web-tab-fold.left { left: 198px; }
  .web-tab-fold.right { left: 346px; }

  /* Card front */
  .card-front .base-band {
    position: absolute; left: 0; right: 0; bottom: 0; height: 23px;
    background: radial-gradient(ellipse 50% 150% at 50% 50%, #9b8d7f, var(--taupe) 85%);
  }
  .card-front .web-pill {
    position: absolute; left: 79px; top: 118px; width: 89px; height: 14px;
    background: var(--slate); border-radius: 3px;
    color: var(--white); font-size: 5.5px;
    display: flex; align-items: center; justify-content: center;
  }

  /* Card back */
  .card-back .side-band {
    position: absolute; left: 24px; top: 0; width: 93px; height: 143px;
    background: linear-gradient(180deg, #837464, var(--taupe-dark));
    color: var(--white); font-size: 4.6px; font-weight: 600; line-height: 1.25;
  }
  .card-back .icon-rail {
    position: absolute; left: 20px; top: 24px; width: 26px; height: 88px;
    background: var(--slate); border-radius: 6px;
  }
  .card-back .icon-rail .icon { position: absolute; left: 8.5px; width: 9px; height: 9px; }
  .card-back .icon-rail .icon.pin { top: 13px; }
  .card-back .icon-rail .icon.mail { top: 41px; }
  .card-back .icon-rail .icon.tel { top: 61px; }
  .card-back .detail { position: absolute; left: 26px; white-space: nowrap; }
  .card-back .detail.address { top: 38px; }
  .card-back .detail.mail { top: 68px; }
  .card-back .detail.tel { top: 88px; }
  .card-back .detail.site { top: 125px; left: 16px; }
  .card-back .holder { position: absolute; right: 22px; top: 100px; text-align: right; }
  .card-back .holder-name { color: var(--ink-grey); font-size: 10px; font-weight: 400; letter-spacing: 0.02em; }
  .card-back .holder-role { color: var(--taupe-dark); font-size: 4.8px; font-weight: 700; }

  /* Envelope */
  .address-window {
    position: absolute; left: 326px; top: 132px; width: 233px; height: 102px;
    border: 1.3px solid var(--window-line); border-radius: 11px;
  }
  .envelope-flap { position: absolute; left: 7px; top: 7px; width: 570px; height: 82px; }
</style>
</head>
<body>

<svg width="0" height="0" style="position:absolute" aria-hidden="true">
  <defs>
    <symbol id="icon-pin" viewBox="0 0 12 12">
      <circle cx="6" cy="6" r="6" fill="#6c5f52"/>
      <path d="M6 2.6a2.2 2.2 0 0 0-2.2 2.2C3.8 6.5 6 9.2 6 9.2s2.2-2.7 2.2-4.4A2.2 2.2 0 0 0 6 2.6z" fill="#fff"/>
      <circle cx="6" cy="4.8" r="0.8" fill="#6c5f52"/>
    </symbol>
    <symbol id="icon-phone" viewBox="0 0 12 12">
      <circle cx="6" cy="6" r="6" fill="#6c5f52"/>
      <path d="M4 3.1l1.1 1.5-.6.8c.4.9 1.1 1.6 2 2l.8-.6 1.5 1.1-.6 1.1c-2.3-.2-4.1-2-4.3-4.3z" fill="#fff"/>
    </symbol>
    <symbol id="icon-mail" viewBox="0 0 12 12">
      <circle cx="6" cy="6" r="6" fill="#6c5f52"/>
      <rect x="3.2" y="4" width="5.6" height="4" rx="0.4" fill="#fff"/>
      <path d="M3.3 4.2L6 6.2l2.7-2" fill="none" stroke="#6c5f52" stroke-width="0.6"/>
    </symbol>
  </defs>
</svg>

<!-- Letterhead -->
<section class="sheet letterhead">
  <div class="wordmark"><span class="wordmark-square"></span><span>Tidewell Vertical Estate Council</span></div>
  <footer class="contact-band">
    <span class="contact-item address"><svg class="icon"><use href="#icon-pin"/></svg>Yourstreet Address No. 1 - Yourcity 12345 - Country</span>
    <span class="contact-item phone"><svg class="icon"><use href="#icon-phone"/></svg>+0 1234 5678 9012</span>
    <span class="contact-item email"><svg class="icon"><use href="#icon-mail"/></svg>contact@youremail.com</span>
  </footer>
  <svg class="web-tab-fold left" viewBox="0 0 10 13" aria-hidden="true"><polygon points="10,0 10,13 0,13" fill="var(--taupe-fold)"/></svg>
  <svg class="web-tab-fold right" viewBox="0 0 10 13" aria-hidden="true"><polygon points="0,0 0,13 10,13" fill="var(--taupe-fold)"/></svg>
  <div class="web-tab">www.yourwebsite.com</div>
</section>

<!-- Business card, front -->
<section class="sheet card-front">
  <div class="wordmark"><span class="wordmark-square"></span><span>Tidewell Vertical Estate Council</span></div>
  <div class="base-band"></div>
  <div class="web-pill">www.yourwebsite.com</div>
</section>

<!-- Business card, back -->
<section class="sheet card-back">
  <div class="side-band">
    <div class="detail address">First Address Line<br>Second Address Line<br>City, 12345</div>
    <div class="detail mail">contact@email.com</div>
    <div class="detail tel">+0 1234 5678 9012</div>
    <div class="detail site">www.yourwebsite.com</div>
  </div>
  <div class="icon-rail">
    <svg class="icon pin"><use href="#icon-pin"/></svg>
    <svg class="icon mail"><use href="#icon-mail"/></svg>
    <svg class="icon tel"><use href="#icon-phone"/></svg>
  </div>
  <div class="wordmark"><span class="wordmark-square"></span><span>Tidewell Vertical Estate Council</span></div>
  <div class="holder">
    <div class="holder-name">JOHN SMITH</div>
    <div class="holder-role">Vice President - Co-Founder</div>
  </div>
</section>

<!-- Envelope, front -->
<section class="sheet envelope-front">
  <div class="wordmark"><span class="wordmark-square"></span><span>Tidewell Vertical Estate Council</span></div>
  <div class="address-window"></div>
  <footer class="contact-band">
    <span class="contact-item address"><svg class="icon"><use href="#icon-pin"/></svg>Yourstreet Address No. 1 - Yourcity 12345 - Country</span>
    <span class="contact-item phone"><svg class="icon"><use href="#icon-phone"/></svg>+0 1234 5678 9012</span>
    <span class="contact-item email"><svg class="icon"><use href="#icon-mail"/></svg>contact@youremail.com</span>
  </footer>
</section>

<!-- Envelope, back -->
<section class="sheet envelope-back">
  <svg class="envelope-flap" viewBox="0 0 570 82" aria-hidden="true">
    <defs>
      <radialGradient id="flap-shade" cx="285" cy="41" r="285" gradientUnits="userSpaceOnUse" gradientTransform="translate(0 20.5) scale(1 0.5)">
        <stop offset="0" stop-color="#d3d6d5"/>
        <stop offset="0.75" stop-color="#8a979b"/>
      </radialGradient>
    </defs>
    <path d="M0 0H570L554 52Q545 82 515 82H45Q22 82 15 52Z" fill="url(#flap-shade)"/>
  </svg>
  <div class="wordmark"><span class="wordmark-square"></span><span>Tidewell Vertical Estate Council</span></div>
</section>

</body>
</html>
```